Company or website name
- Harwood & Beale LLP
- Links to the website
- harwoodbeale-example.com
- Describe your company and organization and target audience
- lawyers and clients in the need of lawyer for defective products etc
- The design should have the following
- yes
- Other Facts

```html
<!DOCTYPE html>
<html lang="en">
<head>
<meta charset="utf-8">
<title>Harwood &amp; Beale LLP</title>
<link rel="stylesheet" href="https://fonts.googleapis.com/css2?family=Lato:wght@400;700;900&display=swap">
<style>
:root{
  --navy:#1f2a8c;
  --navy-deep:#17206f;
  --navy-light:#4a56ad;
  --sky-top:#dfe6f2;
  --sky-bottom:#94a9d2;
  --nav-top:#6a6a6a;
  --nav-bottom:#3c3c3c;
  --nav-divider:#7d7d7d;
  --page:#f4f5f7;
  --white:#ffffff;
  --text:#3f4350;
  --muted:#6b6f7a;
  --grey-tab:#565656;
}
*{box-sizing:border-box;margin:0;padding:0}
html,body{width:1200px;height:733px;overflow:hidden}
body{font-family:"Lato",sans-serif;background:var(--page);color:var(--text);position:relative}
.top-bar{position:absolute;left:0;top:0;width:1200px;height:34px;background:linear-gradient(90deg,var(--navy-deep),var(--navy) 50%,var(--navy-light));color:var(--white);font-size:11px;font-weight:700}
.top-bar .date{position:absolute;left:155px;top:11px}
.top-bar .utility{position:absolute;right:155px;top:11px;display:flex;gap:10px;letter-spacing:.3px}
.top-bar .sep{opacity:.7}
.site-header{position:absolute;left:0;top:34px;width:1200px;height:103px;background:linear-gradient(var(--white),#eef0f4)}
.brand{position:absolute;left:155px;top:38px;display:flex;align-items:center;gap:10px;font-size:22px;font-weight:700;color:var(--navy);letter-spacing:.5px}
.brand-mark{width:14px;height:14px;border-radius:50%;background:var(--navy)}
.call{position:absolute;right:155px;top:43px;font-size:14px;color:var(--muted)}
.call strong{color:var(--navy);font-weight:700}
.sky-band{position:absolute;left:0;top:160px;width:1200px;height:349px;background:linear-gradient(var(--sky-top),var(--sky-bottom))}
.main-nav{position:absolute;left:155px;top:137px;width:890px;height:50px;background:linear-gradient(var(--nav-top),var(--nav-bottom));display:flex}
.main-nav a{display:block;width:110px;line-height:50px;text-align:center;color:var(--white);font-size:14px;text-decoration:none;border-right:1px solid var(--nav-divider)}
.main-nav a.active{background:var(--navy);width:105px}
.search{position:absolute;right:8px;top:9px;width:190px;height:32px;background:var(--white);border-radius:3px}
.search svg{position:absolute;right:8px;top:8px}
.hero{position:absolute;left:155px;top:187px;width:890px;height:322px}
.hero-photo{position:absolute;inset:0;background:linear-gradient(90deg,#cfd8e2 0%,#aebdcb 35%,#8e9fb2 60%,#c4ccd6 85%,#dfe4ea 100%)}
.hero-panel{position:absolute;left:76px;top:63px;width:357px;height:190px;background:rgba(255,255,255,.82);padding:20px 24px}
.hero-panel h1{font-size:30px;font-weight:400;color:#2a2f45;letter-spacing:.5px;white-space:nowrap}
.hero-panel h1 b{color:var(--navy);font-weight:900}
.hero-panel .rule{width:300px;height:2px;background:var(--navy);margin:8px 0 12px}
.hero-panel p{font-size:13px;line-height:1.35;color:#333}
.btn{display:inline-block;margin-top:20px;width:158px;height:32px;line-height:32px;text-align:center;background:var(--navy);color:var(--white);font-size:11px;font-weight:700;letter-spacing:1.5px;border-radius:2px}
.slide-arrow{position:absolute;top:143px;width:36px;height:36px;border-radius:50%;border:1px solid rgba(255,255,255,.6)}
.slide-arrow.prev{left:10px}
.slide-arrow.next{right:10px}
.about{position:absolute;left:155px;top:535px;width:630px}
.about h2{font-size:14px;font-weight:700;color:#333;letter-spacing:.5px}
.about h2 span{color:var(--navy);margin-left:8px}
.about p{font-size:10.5px;line-height:1.45;margin-top:10px;color:var(--muted)}
.about .more{display:block;text-align:right;font-size:10px;font-weight:700;color:var(--navy);margin-top:8px}
.case-studies{position:absolute;left:820px;top:522px;width:225px;height:150px;background:var(--white);box-shadow:0 1px 4px rgba(0,0,0,.15);padding:12px 16px}
.case-studies h3{text-align:center;font-size:14px;color:var(--navy);font-weight:700;letter-spacing:.5px;border-bottom:1px solid #ddd;padding-bottom:6px}
.case-studies ul{list-style:none;margin-top:8px;border-right:3px solid var(--navy);padding-right:8px}
.case-studies li{font-size:9.5px;line-height:1.3;color:var(--navy);margin-bottom:7px}
.services{position:absolute;left:155px;top:690px;width:890px;display:flex;gap:20px}
.service{width:283px}
.service h4{height:28px;line-height:28px;text-align:center;color:var(--white);background:var(--grey-tab);font-size:11px;font-weight:700;letter-spacing:.5px}
.service.featured h4{background:var(--navy)}
.service-photo{height:60px;background:linear-gradient(#7a4a2a,#c0703a 50%,#6b3e22)}
</style>
</head>
<body>
<div class="top-bar">
  <span class="date">June 12, 2014</span>
  <nav class="utility"><span>SUBMIT QUERY</span><span class="sep">|</span><span>FAQS</span><span class="sep">|</span><span>HELP</span><span class="sep">|</span><span>ARTICLES</span></nav>
</div>
<header class="site-header">
  <div class="brand"><span class="brand-mark"></span>HARWOOD &amp; BEALE LLP</div>
  <div class="call">Call us <strong>800 555 0142</strong></div>
</header>
<div class="sky-band"></div>
<nav class="main-nav">
  <a class="active" href="#">HOME</a><a href="#">SERVICES</a><a href="#">NEWS</a><a href="#">ABOUT</a><a href="#">CONTACT</a><a href="#">HELP</a>
  <div class="search"><svg width="16" height="16" viewBox="0 0 16 16"><circle cx="6.5" cy="6.5" r="5" fill="none" stroke="#1f2a8c" stroke-width="2"/><line x1="10" y1="10" x2="15" y2="15" stroke="#1f2a8c" stroke-width="2.4"/></svg></div>
</nav>
<section class="hero">
  <div class="hero-photo" role="img" aria-label="City skyline over water with a smiling lawyer in a suit pointing upward"></div>
  <span class="slide-arrow prev"></span><span class="slide-arrow next"></span>
  <div class="hero-panel">
    <h1>NEED A <b>LAWYER ??</b></h1>
    <div class="rule"></div>
    <p>This is Draftsuite's version of Lorem Ipsum. Proin gravida nibh vel velit auctor aliquet.</p>
    <span class="btn">KNOW MORE</span>
  </div>
</section>
<section class="about">
  <h2>ABOUT<span>HARWOOD &amp; BEALE LLP</span></h2>
  <p>This is Draftsuite's version of Lorem Ipsum. Proin gravida nibh vel velit auctor aliquet. Aenean sollicitudin, lorem quis bibendum auctor, nisi elit consequat ipsum, nec sagittis sem nibh id elit. Duis sed odio sit amet nibh vulputate cursus a sit amet mauris. Morbi accumsan ipsum velit.</p>
  <p>Nam nec tellus a odio tincidunt auctor a ornare odio. Sed non mauris vitae erat consequat auctor eu in elit. Class aptent taciti sociosqu ad litora torquent per conubia nostra, per inceptos himenaeos.</p>
  <span class="more">Know more &gt;&gt;</span>
</section>
<aside class="case-studies">
  <h3>CASE STUDIES</h3>
  <ul>
    <li>This is Draftsuite's version of Lorem Ipsum. Proin gravida nibh vel velit auctor aliquet.</li>
    <li>Aenean sollicitudin, lorem quis bibendum auctor, nisi elit consequat ipsum, nec sagittis.</li>
    <li>Duis sed odio sit amet nibh vulputate cursus a sit amet.</li>
  </ul>
</aside>
<section class="services">
  <div class="service featured"><h4>SERVICE SPECIFICATION</h4><div class="service-photo" role="img" aria-label="Wood-panelled courtroom interior"></div></div>
  <div class="service"><h4>SERVICE SPECIFICATION</h4><div class="service-photo" role="img" aria-label="Wood-panelled courtroom interior"></div></div>
  <div class="service"><h4>SERVICE SPECIFICATION</h4><div class="service-photo" role="img" aria-label="Wood-panelled courtroom interior"></div></div>
</section>
</body>
</html>
```